K & R Ground Works. Business card design

We need a business card designed for a new business. We have a bulldozer and tractor service. We clear land and make wildlife food plots. We provide disking, bush hogging, and site prep services.
I have attached an image of a business card that I like and would like my business cards to look similar.

Target Market(s)

anyone needing bulldozer and/or tractor services

Industry/Entity Type

Business

Contact Information for Business Card

K & R Ground Works, Operated by 7-T-Ranch
Dale Whitcomb
601-555-0148
dwk4821@mailbarn.example

Font styles to use
Sans Serif

Colors

Designer to choose colors to be used in the design.

Requirements
Must have
• image of tractor and bulldozer
• Land Clearing
• Wildlife food plots
• Bush Hogging
• Disking
• Site prep
Nice to have
• i have included a image of a business card that i like. I would like mine to be similar.

```html
<!DOCTYPE html>
<html lang="en">
<head>
<meta charset="utf-8">
<title>K &amp; R Ground Works – Business Card</title>
<link rel="stylesheet" href="https://fonts.googleapis.com/css2?family=Bebas+Neue&family=Roboto:wght@400&display=swap">
<style>
  :root {
    --page-bg: #3a2e22;
    --band-black: #000000;
    --accent-red: #e3191f;
    --text-white: #ffffff;
    --photo-forest: #1e3315;
    --photo-grass: #3f4a26;
    --photo-ground: #4a3e2a;
    --photo-tractor: #c4442a;
    --photo-tractor-deep: #8e2f1d;
    --photo-shade: rgba(0, 0, 0, 0.28);
  }
  * { box-sizing: border-box; margin: 0; padding: 0; }
  html, body {
    width: 1200px;
    height: 930px;
    overflow: hidden;
    background: var(--page-bg);
  }
  .card {
    position: absolute;
    left: 80px;
    top: 168px;
    width: 1040px;
    height: 594px;
    border-radius: 34px;
    overflow: hidden;
    background: var(--photo-forest);
    color: var(--text-white);
  }
  .card-header {
    position: absolute;
    left: 0; top: 0;
    width: 100%;
    height: 84px;
    background: var(--band-black);
    display: flex;
    align-items: center;
    justify-content: center;
    font-family: "Bebas Neue", sans-serif;
    font-size: 44px;
    letter-spacing: 0.3px;
    padding-top: 6px;
  }
  .header-rule {
    position: absolute;
    left: 0; top: 84px;
    width: 100%;
    height: 9px;
    background: var(--accent-red);
  }
  .tractor-photo {
    position: absolute;
    left: 0; top: 93px;
    width: 100%;
    height: 501px;
    background:
      linear-gradient(var(--photo-shade), var(--photo-shade)),
      radial-gradient(ellipse 20% 26% at 60% 38%, var(--photo-tractor) 0%, rgba(196,68,42,0.6) 55%, transparent 100%),
      radial-gradient(ellipse 24% 20% at 62% 76%, var(--photo-tractor) 0%, rgba(196,68,42,0.55) 60%, transparent 100%),
      radial-gradient(ellipse 14% 30% at 25% 62%, var(--photo-tractor-deep) 0%, rgba(142,47,29,0.5) 60%, transparent 100%),
      radial-gradient(ellipse 40% 50% at 50% 60%, var(--photo-tractor-deep) 0%, rgba(142,47,29,0.35) 60%, transparent 100%),
      linear-gradient(180deg, var(--photo-forest) 0%, #2c4420 35%, var(--photo-grass) 70%, var(--photo-ground) 100%);
  }
  .services {
    position: absolute;
    right: 601px;
    top: 270px;
    text-align: right;
    list-style: none;
    font-family: "Bebas Neue", sans-serif;
    font-size: 41px;
    line-height: 44px;
  }
  .divider {
    position: absolute;
    left: 492px;
    top: 277px;
    width: 3px;
    height: 162px;
    background: var(--text-white);
  }
  .contact {
    position: absolute;
    left: 534px;
    top: 268px;
  }
  .contact-name {
    font-family: "Bebas Neue", sans-serif;
    font-size: 76px;
    line-height: 76px;
    font-weight: 400;
  }
  .contact-line {
    display: flex;
    align-items: center;
    font-family: "Roboto", sans-serif;
    font-size: 32px;
    line-height: 45px;
  }
  .contact-line svg {
    width: 22px;
    height: 22px;
    margin: 0 18px 0 2px;
    flex: none;
  }
</style>
</head>
<body>
  <div class="card">
    <div class="tractor-photo" role="img" aria-label="Photo of a red tractor with front loader working in a cleared field edged by trees"></div>
    <header class="card-header">K &amp; R Ground Works, Operated by 7-T-Ranch</header>
    <div class="header-rule"></div>

    <ul class="services">
      <li>Land Clearing</li>
      <li>Wildlife Food Plots</li>
      <li>Bush Hogging</li>
      <li>Disking – Site Prep</li>
    </ul>

    <div class="divider"></div>

    <div class="contact">
      <h1 class="contact-name">Dale Whitcomb</h1>
      <p class="contact-line">
        <svg viewBox="0 0 24 24" aria-hidden="true"><path fill="#fff" d="M6.6 2.5c.6-.3 1.3 0 1.6.6l1.6 3.3c.3.6.1 1.2-.4 1.6L8 9c.9 2.4 2.6 4.6 4.8 6l1-1.3c.4-.5 1.1-.6 1.6-.3l3.1 1.9c.6.3.8 1.1.4 1.7l-1.2 2.1c-.4.7-1.2 1-2 .8C9.6 18.4 5 12.5 4.9 5.6c0-.8.4-1.5 1.1-1.9z"/></svg>
        601-555-0148
      </p>
      <p class="contact-line">
        <svg viewBox="0 0 24 24" aria-hidden="true"><rect x="2.5" y="5.5" width="19" height="13" rx="1.5" fill="none" stroke="#fff" stroke-width="2"/><path d="M3 6.5l9 6.5 9-6.5" fill="none" stroke="#fff" stroke-width="2"/></svg>
        dwk4821@mailbarn.example
      </p>
    </div>
  </div>
</body>
</html>
```